business card design for a plumbing contractor

i need a double business card for a plumbing business, our initial service is residential Sewer Drain Cleaning.

Target Market(s)

other plumbing Business

Industry/Entity Type

Plumbing

Contact Information for Business Card

www.PipeworksCrestline.example- 5817302946-

Font styles to use
Serif

Colors
ec1f27
0455a3

```html
<!DOCTYPE html>
<html lang="en">
<head>
<meta charset="utf-8">
<title>Pipeworks Crestline – Business Card</title>
<link rel="stylesheet" href="https://fonts.googleapis.com/css2?family=Roboto+Condensed:wght@400;700&family=Roboto:wght@400&display=swap">
<style>
  :root {
    --backdrop: #2a2a2a;
    --card-red: #d63531;
    --card-white: #efefef;
    --ink-white: #ffffff;
    --ink-taupe: #7b7164;
    --accent-red: #e23a33;
  }
  * { margin: 0; padding: 0; box-sizing: border-box; }
  html, body {
    width: 1200px; height: 960px; overflow: hidden;
    background: var(--backdrop);
  }
  .canvas { position: relative; width: 1200px; height: 960px; }
  .card {
    position: absolute; width: 600px; height: 343px;
    box-shadow: 0 3px 6px rgba(0,0,0,0.45);
  }
  .card--front { left: 322px; top: 108px; background: var(--card-red); color: var(--ink-white); }
  .card--back { left: 320px; top: 493px; background: var(--card-white); }

  .identity {
    position: absolute; right: 104px; top: 50px; text-align: right;
    font-family: "Roboto Condensed", sans-serif; font-weight: 700; line-height: 1;
  }
  .identity__name { font-size: 23px; letter-spacing: 0.3px; }
  .identity__title { font-size: 15px; margin-top: 4px; letter-spacing: 0.3px; }
  .identity__mark {
    position: absolute; right: 40px; top: 44px;
    width: 44px; height: 44px; background: var(--ink-white);
  }

  .contact {
    position: absolute; left: 31px; top: 222px;
    font-family: "Roboto Condensed", sans-serif; font-size: 14px; line-height: 18px;
  }
  .services {
    position: absolute; left: 31px; top: 281px;
    font-family: "Roboto", sans-serif; font-size: 14px; line-height: 18px;
    list-style: none;
  }
  .services li { display: inline; }
  .services li::before { content: "\2022"; margin-right: 4px; }
  .services .line-break { display: block; }

  .brand {
    position: absolute; left: 150px; top: 128px;
    display: flex; align-items: center; gap: 14px;
  }
  .brand__name {
    font-family: "Roboto Condensed", sans-serif; font-weight: 700;
    font-size: 38px; line-height: 36px; color: var(--ink-taupe); text-align: right;
  }
  .brand__mark { width: 70px; height: 70px; background: var(--accent-red); }
</style>
</head>
<body>
<div class="canvas">
  <section class="card card--front">
    <div class="identity">
      <div class="identity__name">MARK ELLISON</div>
      <div class="identity__title">CEO/FOUNDER</div>
    </div>
    <div class="identity__mark"></div>
    <div class="contact">
      <div>P : 5817302946</div>
      <div>Dispatcher@PipeworksCrestline.example</div>
      <div>www.PipeworksCrestline.example</div>
    </div>
    <ul class="services">
      <li class="line-break">Sewer Drain Cleaning</li>
      <li>Maintenance</li>&nbsp;
      <li>Trenchless Pipe Installs</li>
    </ul>
  </section>

  <section class="card card--back">
    <div class="brand">
      <div class="brand__name">Pipeworks<br>Crestline</div>
      <div class="brand__mark"></div>
    </div>
  </section>
</div>
</body>
</html>
```